Orlo Novelties

We need a web design for an ecommerce website that sells innovative gadgets. ***We are in the early stages of the business and don't have official products yet, they are being created. so we need to use placeholders and fake content, please email me with any questions regarding this.

The web page must look modern, fresh and simple and include-

• Logo
• My Account & View Cart link
• Menu - Home, Shop, The Latest, About Us, FAQ, Blog, Contact Us
• Promo bar at the top of the page like on: http://www.larkandfern.com/lkfn/ (you can use placeholder text for now)
• Search Box
• Chatterloom, Quipsy, Vidarrow, Snipboard and Orbix+ icons
• Slogan “Amaze your friends”
• Free shipping on orders over $50
• Banner section - for now you can highlight one of the fake products below, focus on free shipping on order over $50 or some kind of fake promotion
• New Arrivals section - highlight these fake products since we don't have products yet so you can use these products as place holders-
1. https://www.thebramblecart.com/tech-gadgets/the-zuvvet
2. https://www.thebramblecart.com/tech-gadgets/plinzo-cord-keeper
3. https://www.thebramblecart.com/tech-gadgets/ventrosk-padsofts
• credit card logos
• payvoucha.net seal - https://check.payvoucha.net/pvseal/images/secure90x72.gif

Example websites:
http://www.larkandfern.com/lkfn/
https://www.thebramblecart.com/
http://www.velmstacks.com/
https://plovewick.co/
http://zentrioworks.com/
http://www.dulvaroltd.com/
http://www.quessary.com/

• • Logo
• Search Box
• credit card logos

```html
<!DOCTYPE html>
<html lang="en">
<head>
<meta charset="utf-8">
<title>Orlo Novelties</title>
<link rel="stylesheet" href="https://fonts.googleapis.com/css2?family=Open+Sans:wght@400;600;700&family=Raleway:wght@400;500&display=swap">
<style>
:root{
  --sky:#45b0df;
  --navy:#1c2f63;
  --navy-band:rgba(22,48,104,.9);
  --ink:#333;
  --page:#ffffff;
  --footer:#202020;
  --hero-a:#f6f6f6;
  --hero-b:#dcdcdc;
}
*{margin:0;padding:0;box-sizing:border-box}
html,body{width:690px;height:1200px;overflow:hidden;background:var(--page)}
body{position:relative;font-family:"Open Sans",sans-serif;color:var(--ink)}
.abs{position:absolute}
.promo-bar{left:0;top:0;width:690px;height:22px;background:var(--sky);color:#fff;font-size:7px;font-weight:600;line-height:22px;padding-left:70px}
.brand{left:70px;top:44px;display:flex;align-items:center;gap:6px}
.brand-dot{width:30px;height:30px;border-radius:50%;background:var(--sky)}
.brand-name{font-size:15px;font-weight:700;color:var(--navy)}
.search-box{left:246px;top:45px;width:219px;height:22px;border:1px solid #d4d4d4;border-radius:3px;background:#f4f4f4}
.search-box svg{position:absolute;right:8px;top:5px}
.account-links{left:532px;top:52px;font-size:7px;color:var(--navy)}
.account-links span{margin:0 4px}
.main-nav{left:68px;top:101px;width:552px;height:29px;background:linear-gradient(#fff,#f4f4f4);box-shadow:0 1px 3px rgba(0,0,0,.3);border-radius:2px}
.main-nav a{position:absolute;top:9px;font-size:8px;color:#222;text-decoration:none;transform:translateX(-50%);white-space:nowrap}
.hero{left:69px;top:140px;width:551px;height:269px;background:radial-gradient(circle at 45% 40%,var(--hero-a),var(--hero-b))}
.hero-title{left:49px;top:36px;font-family:"Raleway",sans-serif;font-size:17px;color:var(--navy)}
.hero-product{left:71px;top:88px;width:232px;height:148px;background:linear-gradient(90deg,#2a7f9c,#222 45%,#b8265a);border-radius:6px;opacity:.85}
.hero-offer{left:332px;top:118px;font-family:"Raleway",sans-serif;font-size:15px;color:#222;line-height:26px}
.hero-price{left:447px;top:124px;font-family:"Raleway",sans-serif;font-size:33px;color:var(--sky)}
.hero-arrow{top:124px;width:19px;height:20px;background:#fff}
.hero-arrow svg{display:block;margin:5px auto}
.section-title{left:0;width:690px;text-align:center;font-family:"Raleway",sans-serif;font-weight:500;font-size:17px;color:var(--navy)}
.product-card{width:164px;height:177px;overflow:hidden}
.product-photo{width:100%;height:100%}
.product-caption{position:absolute;left:0;bottom:0;width:100%;height:32px;background:var(--navy-band);color:#fff;font-size:9.5px;font-weight:600;line-height:32px;padding-left:7px;white-space:nowrap}
.play-btn{position:absolute;left:53px;top:66px;width:47px;height:33px;border-radius:7px;background:rgba(20,20,20,.85)}
.play-btn svg{display:block;margin:9px auto}
.latest-intro{left:69px;top:929px;width:225px;height:137px;background:var(--sky);color:#fff;padding:16px 15px}
.latest-intro h3{font-weight:400;font-size:10px;margin-bottom:14px}
.latest-intro p{font-size:7px;line-height:9px;width:180px}
.see-all{position:absolute;left:13px;top:98px;width:65px;height:19px;background:var(--navy);border-radius:3px;color:#fff;font-size:7px;text-align:center;line-height:19px}
.latest-photo{top:929px;height:137px}
.site-footer{left:0;top:1089px;width:690px;height:111px;background:var(--footer)}
.pay-cards{left:226px;top:29px;display:flex;gap:4px}
.pay-card{width:25px;height:16px;background:#fff;border-radius:2px;font-size:5px;font-weight:600;color:var(--navy);text-align:center;line-height:16px;white-space:nowrap;overflow:hidden}
.secure-seal{left:433px;top:21px;width:32px;height:32px;border-radius:50%;background:#d9b93a}
.footer-links{left:0;top:60px;width:690px;text-align:center;font-size:7.5px;color:#fff}
.footer-links span{margin:0 5px}
.copyright{left:0;top:80px;width:690px;text-align:center;font-size:7.5px;color:var(--sky)}
</style>
</head>
<body>
<div class="abs promo-bar">Aenean sollicitudin, lorem quis bibendum auctor, nisi elit consequat ipsum Proin gravida nibh vel velit auctor aliquet.</div>

<div class="abs brand"><div class="brand-dot"></div><div class="brand-name">Orlo Novelties</div></div>

<div class="abs search-box"><svg width="14" height="11" viewBox="0 0 14 11"><circle cx="5" cy="5" r="3.5" fill="none" stroke="#bbb" stroke-width="1.3"/><line x1="7.6" y1="7" x2="12" y2="10" stroke="#bbb" stroke-width="1.6"/></svg></div>

<div class="abs account-links">My Account<span>|</span>View Cart</div>

<nav class="abs main-nav">
  <a style="left:79px">Home</a><a style="left:138px">Shop</a><a style="left:205px">The Latest</a><a style="left:280px">About Us</a><a style="left:343px">FAQ</a><a style="left:398px">Blog</a><a style="left:465px">Contact Us</a>
</nav>

<section class="abs hero">
  <div class="abs hero-title">Amaze Your Friends</div>
  <div class="abs hero-product" role="img" aria-label="Three smartphone cases in teal, black and pink"></div>
  <div class="abs hero-offer">Free shipping<br>on orders over</div>
  <div class="abs hero-price">$50</div>
  <div class="abs hero-arrow" style="left:0"><svg width="7" height="10"><polyline points="6,0 1,5 6,10" fill="none" stroke="#333"/></svg></div>
  <div class="abs hero-arrow" style="right:0"><svg width="7" height="10"><polyline points="1,0 6,5 1,10" fill="none" stroke="#333"/></svg></div>
</section>

<h2 class="abs section-title" style="top:439px">New Arrivals</h2>

<div class="abs product-card" style="left:69px;top:476px"><div class="product-photo" role="img" aria-label="Carabiner hook clipped to a rail" style="background:linear-gradient(160deg,#cfe3ef,#5f7f9a 60%,#2c3a4c)"></div><div class="play-btn"><svg width="12" height="14"><polygon points="0,0 12,7 0,14" fill="#fff"/></svg></div><div class="product-caption">CARABINER HOOK</div></div>
<div class="abs product-card" style="left:263px;top:476px"><div class="product-photo" role="img" aria-label="Green screen cleaner held in a hand" style="background:linear-gradient(160deg,#d8d8d8,#6b8a5a 50%,#2a2a2a)"></div><div class="play-btn"><svg width="12" height="14"><polygon points="0,0 12,7 0,14" fill="#fff"/></svg></div><div class="product-caption">SCREEN CLEANER</div></div>
<div class="abs product-card" style="left:456px;top:476px"><div class="product-photo" role="img" aria-label="White cables wrapped in a wristband" style="background:linear-gradient(160deg,#8a7560,#d9d6d0 50%,#6e5a48)"></div><div class="play-btn"><svg width="12" height="14"><polygon points="0,0 12,7 0,14" fill="#fff"/></svg></div><div class="product-caption">FLASHDRIVE WRISTBAND</div></div>

<div class="abs product-card" style="left:69px;top:682px"><div class="product-photo" role="img" aria-label="White phone case with a kickstand on a table" style="background:linear-gradient(180deg,#3a3a3a,#e9e9e9 60%,#fafafa)"></div><div class="product-caption">SCREEN CLEANER</div></div>
<div class="abs product-card" style="left:263px;top:682px"><div class="product-photo" role="img" aria-label="Yellow USB wristband beside a laptop" style="background:linear-gradient(170deg,#2e2e2e,#b9b9b9 55%,#d8d8d8)"></div><div class="product-caption">8GB USB FLASHDRIVE WRISTBAND</div></div>
<div class="abs product-card" style="left:456px;top:682px"><div class="product-photo" role="img" aria-label="Gloved hand using a touchscreen phone" style="background:linear-gradient(160deg,#5a5a5a,#a9b4c8 55%,#7d7d7d)"></div><div class="product-caption">TOUCHSCREEN GLOVES</div></div>

<h2 class="abs section-title" style="top:895px">The Latest</h2>

<div class="abs latest-intro">
  <h3>Proin gravida nibh vel velit auctor</h3>
  <p>Aenean sollicitudin, lorem quis bibendum auctor, nisi elit consequat ipsum, nec sagittis sem nibh id elit. Duis sed odio sit amet nibh vulputate cursus a sit amet mauris. Morbi accumsan ipsum velit.</p>
  <div class="see-all">SEE ALL</div>
</div>
<div class="abs latest-photo" role="img" aria-label="Cord keeper next to a computer mouse" style="left:295px;width:161px;background:linear-gradient(150deg,#3a3a3a,#dfe6ea 45%,#c9a77a)"></div>
<div class="abs latest-photo" role="img" aria-label="Earbud cord keeper on a red background" style="left:457px;width:162px;background:linear-gradient(150deg,#7a0d0d,#e7e7e7 55%,#c91c1c)"></div>

<footer class="abs site-footer">
  <div class="abs pay-cards">
    <div class="pay-card">Tallo</div><div class="pay-card">Brinq</div><div class="pay-card">Corvo</div><div class="pay-card">Nimra</div><div class="pay-card">Pelto</div><div class="pay-card">Sarvi</div><div class="pay-card">Quell</div>
  </div>
  <div class="abs secure-seal"></div>
  <div class="abs footer-links">Home<span>|</span>Shop<span>|</span>The Latest<span>|</span>About Us<span>|</span>FAQ<span>|</span>Blog<span>|</span>Contact Us</div>
  <div class="abs copyright">Copyright © 2014 All rights reserved</div>
</footer>
</body>
</html>
```